Taro Velmane Website

I have a client who is a physical therapist who I am redeveloping a website for. The new site will be a combination of two sites, once that handles the practice site of the business and another for the education side of the business in which they will accept online registration for therapeutic training courses for physical therapy students.

The existing sites (just for background purposes) are here:

Private Practice: http://movarelinc.com/
Education: http://peltafoundation.com/

So, the new site will be a modern looking site that combines both the private practice content and the education content (register for classes) information.

The home page should have a clear distinction between private practice and education. I am thinking that a button or icon to view/register for classes somewhere on the Home page would lead users to that section of the website that deals specifically with education.

So, that said, I am think the navigation should include the following:

Home
About Us
Our Services
Education
Contact Us

The client has provided the following websites as examples sites in which they like the colors. Here is the direct quote from the client:

"We were looking for sites that looked comfortable in colors and presentation, please view so you have a better idea what we want the feel and colors to be like

http://www.trelbywanders.com/

http://www.mirtavale.com/

www.dermoquill.com"

Note that all examples they provided have a similar type of layout with a large slideshow image front and center, horizontal navigation and large footer areas with contact information and links to pages and social networks.

I am also going to be working on a logo for them, I have yet to decide on what text that will include or what icons (if any) will be a part of that. I am thinking that the doctor's name "Taro Velmane" but I am still struggling with that so a placeholder logo for now would be fine.

```html
<!DOCTYPE html>
<html lang="en">
<head>
<meta charset="utf-8">
<title>Movarel — Home</title>
<link href="https://fonts.googleapis.com/css2?family=Open+Sans:wght@400;600;700&display=swap" rel="stylesheet">
<style>
:root{
  --orange:#e04a13;
  --orange-dark:#c93d0c;
  --yellow:#f7d51c;
  --text:#555555;
  --heading-dark:#333333;
  --border:#d6d6d6;
  --footer:#464646;
  --footer-bottom:#0f0f0f;
  --blue-link:#2e6ba8;
  --white:#ffffff;
}
*{box-sizing:border-box;margin:0;padding:0}
html,body{width:692px;height:1200px;overflow:hidden}
body{position:relative;background:var(--white);font-family:"Open Sans",sans-serif;color:var(--text);font-size:7px;line-height:1.9}
.abs{position:absolute}

.top-rule{left:0;top:0;width:692px;height:3px;background:var(--orange)}
.site-header{left:0;top:3px;width:692px;height:52px}
.brand{left:58px;top:14px;display:flex;align-items:center;gap:6px;color:var(--orange);font-size:17px;font-weight:600;line-height:1}
.brand-dot{width:12px;height:12px;border-radius:50%;background:var(--orange)}
.main-nav{right:58px;top:15px;display:flex;gap:6px}
.main-nav a{display:block;padding:0 10px;height:21px;line-height:21px;font-size:7.2px;color:#222;text-decoration:none}
.main-nav a.active{background:var(--orange);color:var(--white)}

.hero{left:0;top:55px;width:692px;height:286px;background:linear-gradient(100deg,#8a8f8c 0%,#b9bab3 30%,#a99f93 55%,#6f5a45 80%,#3e342b 100%)}
.hero-caption{left:57px;top:122px;width:308px;height:42px;background:var(--orange);color:var(--white);font-size:13px;line-height:42px;padding-left:11px}
.hero-arrow{top:136px;width:24px;height:24px;border-radius:50%;background:var(--white);display:flex;align-items:center;justify-content:center}
.hero-dots{left:320px;top:268px;display:flex;gap:3px}
.hero-dots span{width:8px;height:8px;border-radius:50%;background:var(--white);border:1px solid #555}
.hero-dots span.on{background:var(--orange)}

.promo-band{left:0;top:341px;width:692px;height:50px;background:var(--orange)}
.promo-text{left:58px;top:11px;width:450px;color:var(--white);font-size:8px;line-height:14px}
.register-btn{left:522px;top:9px;width:112px;height:29px;background:var(--yellow);color:#222;font-size:8px;display:flex;align-items:center;gap:6px;padding-left:6px}

.welcome-title{left:0;top:400px;width:692px;text-align:center;color:var(--orange);font-size:17px;line-height:28px;font-weight:400}
.welcome-copy{left:58px;top:429px;width:576px;text-align:center;font-size:7px;line-height:13.8px}

.card{width:169px;border:1px solid var(--border);background:var(--white)}
.card-head{height:25px;background:var(--orange);color:var(--white);font-size:10px;line-height:25px;padding-left:7px}
.card-body{padding:6px 6px;font-size:6.4px;line-height:13.8px;position:relative}
.btn{display:inline-block;background:var(--orange);color:var(--white);font-size:6.4px;font-weight:700;text-transform:uppercase;line-height:17px;padding:0 7px;border-radius:2px}
.card-icon{position:absolute}

.foundation-title{left:57px;top:662px;color:var(--orange);font-size:14px;line-height:20px}
.foundation-copy{left:57px;top:684px;width:290px;font-size:7.6px;line-height:14px}
.checklist{left:58px;top:738px;list-style:none;font-size:7px;line-height:19.4px;color:#222}
.checklist li{display:flex;align-items:center;gap:8px}
.video-frame{left:388px;top:668px;width:247px;height:161px;border:1px solid var(--border);padding:8px}
.video-art{width:100%;height:100%;background:radial-gradient(circle at 50% 50%,#d8d8d8 0%,#f3f3f3 55%,#ffffff 100%)}

.panel{width:179px;border:1px solid #cfcfcf;border-radius:5px;overflow:hidden;background:var(--white);box-shadow:0 1px 2px rgba(0,0,0,.12)}
.panel-head{height:27px;background:linear-gradient(#e75a1f,var(--orange-dark));color:var(--white);font-size:11px;line-height:27px;padding-left:11px}
.panel-body{height:89px;position:relative;font-size:6.4px;line-height:13px;padding:6px 6px}

.site-footer{left:0;top:998px;width:692px;height:141px;background:var(--footer);color:var(--white)}
.footer-col-title{font-size:10px;line-height:14px}
.footer-copy{font-size:6.3px;line-height:11.3px;margin-top:6px}
.map{left:388px;top:15px;width:247px;height:115px;background:linear-gradient(135deg,#e9e4d6,#d9e2cf 50%,#ede6d3)}

.footer-bottom{left:0;top:1139px;width:692px;height:61px;background:var(--footer-bottom);color:var(--white)}
.footer-links{left:57px;top:16px;font-size:6.4px;line-height:14px}
.socials{left:564px;top:20px;display:flex;gap:5px}
.socials span{width:13px;height:13px;border-radius:2px;background:#5e6b8a}
.socials span:nth-child(2){background:#4a9fd0}
.socials span:nth-child(3){background:#2a6fa0}
.socials span:nth-child(4){background:#e8731c}
</style>
</head>
<body>

<div class="abs top-rule"></div>
<header class="abs site-header">
  <div class="abs brand"><span class="brand-dot"></span>Movarel</div>
  <nav class="abs main-nav">
    <a class="active" href="#">Home</a>
    <a href="#">About Us</a>
    <a href="#">Our Services</a>
    <a href="#">Education</a>
    <a href="#">Contact Us</a>
  </nav>
</header>

<section class="abs hero" role="img" aria-label="Soft-focus photograph of a therapy clinic interior"></section>
<div class="abs hero-caption">Experience a hands-on approach to healing</div>
<div class="abs hero-arrow" style="left:22px"><svg width="10" height="10" viewBox="0 0 10 10"><path d="M6.5 1.5 3 5l3.5 3.5" fill="none" stroke="#222" stroke-width="2"/></svg></div>
<div class="abs hero-arrow" style="left:646px"><svg width="10" height="10" viewBox="0 0 10 10"><path d="M3.5 1.5 7 5 3.5 8.5" fill="none" stroke="#222" stroke-width="2"/></svg></div>
<div class="abs hero-dots"><span class="on"></span><span></span><span></span></div>

<section class="abs promo-band">
  <p class="abs promo-text">One of the world's most comprehensive laser centers, providing state-of-the-art skin laser surgery and industry leading research in a warm, caring environment.</p>
  <a class="abs register-btn">
    <svg width="14" height="14" viewBox="0 0 14 14"><rect x="1.5" y="1.5" width="11" height="11" fill="none" stroke="#222" stroke-width="1.4"/><path d="M4 5h6M4 7.2h6M4 9.4h6" stroke="#222" stroke-width="1.2"/></svg>
    Register for classes
  </a>
</section>

<h1 class="abs welcome-title">Welcome to Movarel</h1>
<p class="abs welcome-copy">Lorem ipsum dolor sit amet, consectetuer adipiscing elit, sed diam nonummy nibh euismod tincidunt ut laoreet dolore magna aliquam erat volutpat. Ut wisi enim ad minim veniam, quis nostrud exerci tation ullamcorper suscipit lobortis nisl ut aliquip ex ea commodo consequat.&nbsp; Lorem ipsum dolor sit amet, consectetuer adipiscing elit, sed diam nonummy nibh euismod tincidunt ut laoreet dolore magna aliquam erat volutpat. Ut wisi enim ad minim veniam, quis nostrud exerci tation ullamcorper suscipit lobortis nisl ut aliquip ex ea commodo consequat.</p>

<article class="abs card" style="left:58px;top:498px;height:147px">
  <div class="card-head">Who we are</div>
  <div class="card-body">At MOVAREL, Inc., we firmly believe that you know your body better than anyone else and everything we do springs from that philosophy. We meld our expertise and experience with your insight to uncover the best route for your physi-cal well-being.</div>
  <span class="abs btn" style="left:5px;top:119px;width:123px">More about Movarel</span>
</article>

<article class="abs card" style="left:263px;top:498px;height:147px">
  <div class="card-head">Next class</div>
  <div class="card-body">Evaluation and Manual Treatment of the Pelvis,<br>Sacrum &amp; Lumbar Spine<br>September 19-21<br>Sacramento, CA</div>
  <svg class="card-icon" style="left:105px;top:54px" width="42" height="42" viewBox="0 0 42 42"><rect x="6" y="7" width="24" height="31" rx="2" fill="none" stroke="#111" stroke-width="3"/><rect x="12" y="3" width="12" height="7" rx="1.5" fill="#111"/><path d="M11 18h10M11 24h8M11 30h6" stroke="#111" stroke-width="2.4"/><path d="M36 10 22 31l-2 6 5-3 14-21z" fill="#111"/></svg>
  <span class="abs btn" style="left:5px;top:119px;width:123px">Upcoming class schedule</span>
</article>

<article class="abs card" style="left:466px;top:498px;height:147px">
  <div class="card-head">2014 schedule</div>
  <div class="card-body">The 2014 class schedule is posted on the Pelta Foundation's website.<br>There you can find:<br>Class schedule<br>Descriptions<br>Accommodations information</div>
  <svg class="card-icon" style="left:108px;top:55px" width="42" height="42" viewBox="0 0 42 42"><path d="M2 8h13l3 4h16v22H2z" fill="#222"/><circle cx="30" cy="31" r="9" fill="#222" stroke="#fff" stroke-width="2"/><path d="M30 26v5h4" stroke="#fff" stroke-width="1.8" fill="none"/></svg>
</article>

<h2 class="abs foundation-title">Movarel Foundation</h2>
<div class="abs foundation-copy">
  <p>Lorem ipsum dolor sit amet, consectetuer adipiscing elit, sed diam nonummy nibh euismod tincidunt ut laoreet dolore</p>
  <p style="margin-top:6px;font-size:7.4px">Lorem ipsum dolor sit amet</p>
</div>
<ul class="abs checklist">
  <li><svg width="9" height="8" viewBox="0 0 9 8"><path d="M1 4.2 3.4 6.5 8 1.2" fill="none" stroke="#2a9a3a" stroke-width="1.6"/></svg>Lorem ipsum</li>
  <li><svg width="9" height="8" viewBox="0 0 9 8"><path d="M1 4.2 3.4 6.5 8 1.2" fill="none" stroke="#2a9a3a" stroke-width="1.6"/></svg>family</li>
  <li><svg width="9" height="8" viewBox="0 0 9 8"><path d="M1 4.2 3.4 6.5 8 1.2" fill="none" stroke="#2a9a3a" stroke-width="1.6"/></svg>Prenatal and postnatal</li>
  <li><svg width="9" height="8" viewBox="0 0 9 8"><path d="M1 4.2 3.4 6.5 8 1.2" fill="none" stroke="#2a9a3a" stroke-width="1.6"/></svg>Lorem ipsum dolor sit amet.</li>
  <li><svg width="9" height="8" viewBox="0 0 9 8"><path d="M1 4.2 3.4 6.5 8 1.2" fill="none" stroke="#2a9a3a" stroke-width="1.6"/></svg>Lorem ipsum dolor sit amet.</li>
</ul>
<div class="abs video-frame"><div class="video-art" role="img" aria-label="Physiotherapy video thumbnail with caring hands illustration and play button"></div></div>

<section class="abs panel" style="left:58px;top:857px">
  <div class="panel-head">Our Faculty</div>
  <div class="panel-body">We are always on the lookout for great people to work with our clients.<br>If you want to be a part of our Team click below to apply.
    <span class="abs btn" style="left:110px;top:60px;font-weight:600">Apply now</span>
  </div>
</section>

<section class="abs panel" style="left:255px;top:857px">
  <div class="panel-head">Testimonials</div>
  <div class="panel-body">
    <div class="abs" role="img" aria-label="Portrait photograph of client Mira Dalen" style="left:6px;top:6px;width:58px;height:62px;background:linear-gradient(160deg,#c78a5e,#e9d6c4 60%,#f4f0ea)"></div>
    <div class="abs" style="left:75px;top:7px;font-size:7.6px;color:var(--blue-link)">Mira Dalen</div>
    <span class="abs btn" style="left:75px;top:30px;font-weight:600">Learn more</span>
  </div>
</section>

<section class="abs panel" style="left:455px;top:857px">
  <div class="panel-head">Latest News</div>
  <div class="panel-body" style="padding-left:12px">
    <div style="color:var(--blue-link);font-weight:700;font-size:6.6px">SPINE RECOVERY HUB</div>
    <div style="margin-top:3px;line-height:15.5px;font-size:6.1px">THE LATEST SPINAL CORD INJURY NEWS,<br>INFORMATION AND RESOURCES FOR PEOPLE</div>
    <span class="abs btn" style="left:14px;top:63px;font-weight:600">Learn more</span>
  </div>
</section>

<footer class="abs site-footer">
  <div class="abs" style="left:58px;top:10px;width:200px">
    <div class="footer-col-title">Movarel</div>
    <p class="footer-copy">Tendwell is proud to be an approved provider for Roadway Injury Board (RIB), Regional Workcare Authority (RWA), Department of Care Services (DCS) and maintain associations and cooperative relationships with a variety of private and governmental organisations in its efforts to bring the finest, most up-to-date care for its clients.</p>
  </div>
  <div class="abs" style="left:272px;top:10px;width:110px">
    <div class="footer-col-title">Contact Us</div>
    <p class="footer-copy">Tendwell - Melbourne<br>212 - 214 Harwick Rd<br>Elmsford Vale<br>Victoria, 3999</p>
    <p class="footer-copy" style="margin-top:8px">(03) 9000 4417</p>
  </div>
  <div class="abs map" role="img" aria-label="Street map showing the clinic location in Melbourne"></div>
</footer>

<div class="abs footer-bottom">
  <div class="abs footer-links">Home &nbsp;|&nbsp; About Us &nbsp;|&nbsp; Products &nbsp;|&nbsp; Contact Us<br>© 2014 Company Name&nbsp; All right reserved&nbsp; Term of Use</div>
  <div class="abs socials" aria-label="Social links"><span></span><span></span><span></span><span></span></div>
</div>

</body>
</html>
```